Investment Advisor Firm Needs a Web Site Design

Brenwick Capital Web Design
We are looking a website design for an Investment Advisor firm in Latin America. Our target is high net clients that are looking for investment solutions such as portfolios and investment opportunities. Colors like gold and black would be preferred. Client will be looking information in our website such as:
• Market Data
• Market Articles
• Market research
• Main commodity products index price
• Indexes and pricing at market
• Audio interviews of top financial speakers in the market
• Educational material
• Investment Objectives
• Latin America top financial news

```html
<!DOCTYPE html>
<html lang="en">
<head>
<meta charset="utf-8">
<title>Brenwick Capital – Investment Advisor</title>
<link rel="stylesheet" href="https://fonts.googleapis.com/css2?family=Mulish:wght@400;600;700&family=Open+Sans:wght@400;600;700&family=Oswald:wght@500;700&display=swap">
<style>
:root{
  --gold:#b8861b;
  --gold-dark:#a97a16;
  --black:#141414;
  --header:#0c0c0c;
  --footer:#1d1d1d;
  --ink:#2a2a2a;
  --muted:#666;
  --light:#f4f4f4;
  --ring:#ececec;
  --white:#fff;
}
*{box-sizing:border-box;margin:0;padding:0}
html,body{width:691px;height:1200px;overflow:hidden;background:var(--white)}
body{position:relative;font-family:"Open Sans",Arial,sans-serif;color:var(--ink)}
.abs{position:absolute}

/* header */
.site-header{left:0;top:0;width:691px;height:72px;background:var(--header)}
.brand{left:57px;top:24px;display:flex;align-items:center;gap:8px}
.brand-mark{width:14px;height:14px;background:var(--gold)}
.brand-name{font-family:"Mulish",sans-serif;font-weight:600;font-size:17px;color:var(--gold);letter-spacing:1px}
.main-nav{left:282px;top:28px;display:flex}
.main-nav a{font-family:"Mulish",sans-serif;font-size:10.4px;color:#ddd;text-decoration:none;padding:0 12px;border-left:1px solid #333;line-height:18px}
.main-nav a:first-child{border-left:none}

/* hero */
.hero-photo{left:0;top:72px;width:691px;height:290px;background:radial-gradient(ellipse at 40% 40%,#6b6b6b 0%,#4a4a4a 55%,#2e2e2e 100%)}
.hero-triangle{left:400px;top:72px}
.hero-title{left:400px;width:288px;text-align:center;font-family:"Oswald",sans-serif;font-weight:700;line-height:1}
.hero-title.t1{top:100px;font-size:41px;color:#2b2b2b;letter-spacing:-.5px}
.hero-title.t2{top:143px;font-size:29px;color:var(--white)}
.hero-text{left:476px;top:182px;width:136px;text-align:center;font-size:7.6px;line-height:13px;color:#2b2b2b}
.hero-arrows{left:525px;top:244px;display:flex;gap:4px}
.hero-arrows span{width:18px;height:18px;border-radius:50%;background:#6d5316;display:block}
.hero-arrows svg{display:block}

/* welcome */
.welcome{left:0;top:362px;width:691px;height:66px;background:var(--light);border-bottom:1px solid #e2e2e2}
.welcome-title{left:57px;top:373px;font-family:"Mulish",sans-serif;font-size:18px;color:var(--black)}
.welcome-sub{left:57px;top:401px;font-size:8.8px;letter-spacing:.2px;color:#333}
.btn-join{left:525px;top:382px;width:108px;height:25px;background:var(--black);color:var(--white);font-size:8.2px;font-weight:600;display:flex;align-items:center;justify-content:center;border-radius:2px}

/* services */
.service{top:468px;width:153px;text-align:center}
.service + .service{border-left:1px solid #f0f0f0}
.service svg{display:block;margin:0 auto}
.service-title{font-family:"Mulish",sans-serif;font-size:12px;color:#2a2a2a;margin-top:10px}
.service-text{font-size:6.3px;line-height:12px;color:var(--muted);margin:6px auto 0;width:128px}
.btn-more{display:inline-block;margin-top:8px;background:var(--gold);color:var(--white);font-size:6.6px;font-weight:600;padding:5px 9px;border-radius:2px}

/* about */
.monitor{left:57px;top:703px;width:256px;height:177px;background:var(--black);border-radius:5px}
.monitor-screen{left:67px;top:713px;width:237px;height:135px;background:linear-gradient(135deg,#d9dde2 0%,#b6bcc3 45%,#3b3b40 75%,#2b2b2e 100%)}
.monitor-chin{left:57px;top:857px;width:256px;height:23px;background:linear-gradient(#dcdcdc,#b8b8b8);border-radius:0 0 5px 5px}
.monitor-neck{left:158px;top:880px;width:54px;height:22px;background:linear-gradient(#c9c9c9,#9d9d9d)}
.monitor-foot{left:141px;top:902px;width:89px;height:5px;background:#aaa;border-radius:3px}
.about-title{left:341px;top:701px;font-family:"Mulish",sans-serif;font-weight:600;font-size:19px;color:var(--black)}
.about-lead{left:340px;top:733px;width:260px;font-size:6.6px;line-height:12.5px;color:#222}
.about-text{left:340px;top:768px;width:295px;font-size:6.3px;line-height:11.7px;color:#555}
.about-list{left:340px;top:823px;width:295px;list-style:none}
.about-list li{font-size:6.2px;color:#333;height:19.5px;line-height:19px;border-bottom:1px solid #ececec;padding-left:14px;position:relative}
.about-list li:last-child{border-bottom:none}
.about-list li::before{content:"";position:absolute;left:0;top:6px;width:4px;height:4px;border:1.5px solid var(--gold);border-radius:50%}

/* gold band */
.gold-band{left:0;top:940px;width:691px;height:134px;background:var(--gold)}
.band-title{top:952px;font-weight:700;font-size:11px;color:var(--white)}
.avatar{left:58px;top:984px;width:68px;height:68px;border-radius:50%;border:3px solid var(--white);background:linear-gradient(#d8dbe0,#5d6978)}
.quote-text{left:142px;top:984px;width:200px;font-size:6.2px;line-height:10.8px;color:var(--white)}
.quote-text b{font-weight:700}
.quote-author{left:142px;top:1035px;font-size:6.4px;font-weight:700;color:var(--white)}
.news-photo{left:386px;top:980px;width:85px;height:73px;background:linear-gradient(135deg,#3d3d3d,#b9a99a 55%,#2f2f2f)}
.news-title{left:481px;top:977px;font-family:"Mulish",sans-serif;font-size:9px;color:var(--white)}
.news-date{left:481px;top:996px;font-size:6.6px;color:var(--white)}
.news-text{left:481px;top:1010px;width:160px;font-size:6.2px;line-height:11px;color:var(--white)}

/* partners */
.partners{left:0;top:1074px;width:691px;height:68px;display:flex;align-items:center;justify-content:space-around;padding:0 50px}
.partners span{font-family:"Mulish",sans-serif;font-weight:700;font-size:15px;color:#8f8f8f}

/* footer */
.site-footer{left:0;top:1142px;width:691px;height:58px;background:var(--footer)}
.footer-links{left:57px;top:1155px;font-size:8px;color:#e5e5e5}
.copyright{left:57px;top:1175px;font-size:6.6px;color:#d0d0d0}
.social{left:555px;top:1164px;display:flex;gap:2px}
.social span{width:14px;height:14px;border:1px solid #cfcfcf;border-radius:50%;display:block}
</style>
</head>
<body>

<header class="abs site-header"></header>
<div class="abs brand"><span class="brand-mark"></span><span class="brand-name">Brenwick Capital</span></div>
<nav class="abs main-nav">
  <a href="#">Home</a><a href="#">About us</a><a href="#">Our Services</a><a href="#">Testimonials</a><a href="#">Contact Us</a>
</nav>

<div class="abs hero-photo" role="img" aria-label="Businessman in a suit facing a concrete wall with a rising growth chart chalked on it"></div>
<svg class="abs hero-triangle" width="288" height="290" viewBox="0 0 288 290"><polygon points="0,0 288,0 144,290" fill="#b8861b"/></svg>
<div class="abs hero-title t1">INVESTMENT</div>
<div class="abs hero-title t2">ADVISOR</div>
<p class="abs hero-text">Lorem ipsum dolor sit amet, consectetur adipiscing elit, sed do eiusmod tempor incididunt ut labore et</p>
<div class="abs hero-arrows">
  <span><svg width="18" height="18" viewBox="0 0 18 18"><path d="M10.5 5 6.5 9l4 4" fill="none" stroke="#fff" stroke-width="1.6"/></svg></span>
  <span><svg width="18" height="18" viewBox="0 0 18 18"><path d="M7.5 5l4 4-4 4" fill="none" stroke="#fff" stroke-width="1.6"/></svg></span>
</div>

<section class="abs welcome"></section>
<h1 class="abs welcome-title">Welcome to Brenwick Capital</h1>
<p class="abs welcome-sub">WE CAN BE YOUR GUIDE TO THE WORLD OF INVESTMENTS</p>
<div class="abs btn-join">JOIN US NOW!</div>

<!-- services -->
<div class="abs service" style="left:39px">
  <svg width="96" height="96" viewBox="0 0 96 96">
    <circle cx="48" cy="48" r="44" fill="none" stroke="#ececec" stroke-width="6"/>
    <path d="M48 4 A44 44 0 0 0 48 92" fill="none" stroke="#b8861b" stroke-width="6"/>
    <path d="M46 33 A16 16 0 1 0 63 50 L46 50Z" fill="#3a3a3a"/>
    <path d="M50 30 A16 16 0 0 1 66 46 L50 46Z" fill="#3a3a3a"/>
  </svg>
  <div class="service-title">Market Data</div>
  <p class="service-text">Lorem ipsum dolor sit amet, conse adipisic ing elit, sed do eiusmod tempor incididunt ut labore et dolore</p>
  <span class="btn-more">READ MORE</span>
</div>
<div class="abs service" style="left:192px">
  <svg width="96" height="96" viewBox="0 0 96 96">
    <circle cx="48" cy="48" r="44" fill="none" stroke="#ececec" stroke-width="6"/>
    <path d="M4 48 A44 44 0 0 1 92 48" fill="none" stroke="#b8861b" stroke-width="6"/>
    <rect x="30" y="36" width="38" height="25" rx="2" fill="none" stroke="#3a3a3a" stroke-width="3"/>
    <rect x="36" y="41" width="10" height="9" fill="#3a3a3a"/>
    <path d="M50 42h13M50 47h13M36 54h27" stroke="#3a3a3a" stroke-width="2.4"/>
  </svg>
  <div class="service-title">Market Articles</div>
  <p class="service-text">Lorem ipsum dolor sit amet, conse adipisic ing elit, sed do eiusmod tempor incididunt ut labore et dolore</p>
  <span class="btn-more">READ MORE</span>
</div>
<div class="abs service" style="left:345px">
  <svg width="96" height="96" viewBox="0 0 96 96">
    <circle cx="48" cy="48" r="44" fill="none" stroke="#ececec" stroke-width="6"/>
    <path d="M48 4 A44 44 0 0 1 48 92" fill="none" stroke="#b8861b" stroke-width="6"/>
    <circle cx="45" cy="45" r="11" fill="none" stroke="#3a3a3a" stroke-width="3.5"/>
    <path d="M53 53l10 10" stroke="#3a3a3a" stroke-width="5" stroke-linecap="round"/>
    <path d="M39 45h12M45 39v12" stroke="#3a3a3a" stroke-width="3"/>
  </svg>
  <div class="service-title">Market research</div>
  <p class="service-text">Lorem ipsum dolor sit amet, conse adipisic ing elit, sed do eiusmod tempor incididunt ut labore et dolore</p>
  <span class="btn-more">READ MORE</span>
</div>
<div class="abs service" style="left:498px">
  <svg width="96" height="96" viewBox="0 0 96 96">
    <circle cx="48" cy="48" r="44" fill="none" stroke="#ececec" stroke-width="6"/>
    <path d="M48 4 A44 44 0 1 0 86 70" fill="none" stroke="#b8861b" stroke-width="6"/>
    <rect x="42" y="30" width="12" height="22" rx="6" fill="#3a3a3a"/>
    <path d="M37 46a11 11 0 0 0 22 0M48 57v6M41 64h14" fill="none" stroke="#3a3a3a" stroke-width="2.5"/>
  </svg>
  <div class="service-title">Financial Speakers</div>
  <p class="service-text">Lorem ipsum dolor sit amet, conse adipisic ing elit, sed do eiusmod tempor incididunt ut labore et dolore</p>
  <span class="btn-more">READ MORE</span>
</div>

<!-- about -->
<div class="abs monitor"></div>
<div class="abs monitor-screen" role="img" aria-label="Team of business people at a meeting table"></div>
<div class="abs monitor-chin"></div>
<div class="abs monitor-neck"></div>
<div class="abs monitor-foot"></div>
<h2 class="abs about-title">ABOUT COMPANY</h2>
<p class="abs about-lead">WE TEACH YOU HOW TO IMPROVE YOUR BUSINESS PROCESSES, AND MAKE THE TECHNOLOGY AFFORDABLE FOR YOU.</p>
<p class="abs about-text">Sed ut perspiciatis unde omnis istes err sit voluptatem accusantium doloremque laudantium, totam rem aperiam, eaque ipsa uae ab illo inventore veritatis et quasi architecto beatae vitae dicta sunt explicabo. Nemo enim ipsam voluptatem quia voluptas sit aspernatur aut odit aut fugit, sed quia conntur magni dolores eos qui ratione voluptatem sequi nesciunt.</p>
<ul class="abs about-list">
  <li>SED UT PERSPICIATIS UNDE OMNIS ISTE</li>
  <li>ACCUSANTIUM DOLOREMQUE LAUDANT</li>
  <li>ROTAM REM APERIAM EAQUE IPSA UAE</li>
  <li>AILLO INVENTORE VERITATIS ET QUASI</li>
</ul>

<!-- testimonials & news -->
<section class="abs gold-band"></section>
<h3 class="abs band-title" style="left:56px">SATISFIED CUSTOMERS</h3>
<div class="abs avatar" role="img" aria-label="Portrait of a satisfied client"></div>
<p class="abs quote-text"><b>“</b>&nbsp; Nulla sollicitudin tincidunt dui et egestas. Phasellus non sem tum, ullamcorper vitae, accumsan dui. Duis dignissim condi lorem. Maecenas facilisis ipsum sed porttitor rutrum. Nulla sollicitudin tincidunt dui et egestas. Phasellus non</p>
<div class="abs quote-author">LENA ARAUJO. NEW YORK &nbsp; ”</div>
<h3 class="abs band-title" style="left:385px">OUR NEWS</h3>
<div class="abs news-photo" role="img" aria-label="Business team gathered at a conference"></div>
<div class="abs news-title">Consectetur Adipisicing Elit</div>
<div class="abs news-date">22 - FEB - 2015</div>
<p class="abs news-text">Praesent vestibulum molestie lacus. Aenean nmmy hendrerit mauris. Phasellus porta. Fusce suscrius mi. Praesent vestibulum molestie lacus. Aenean nonummy hendrerit mauris. Phasellus</p>

<div class="abs partners">
  <span>Corvane</span><span>Talmora</span><span>Vestra</span><span>Lunaro</span><span>Peakline</span><span>Orison</span>
</div>

<footer class="abs site-footer"></footer>
<div class="abs footer-links">Home &nbsp;/&nbsp; About Us &nbsp;/&nbsp; Services &nbsp;/&nbsp; Careers &nbsp;/&nbsp; Contact Us</div>
<div class="abs copyright">©2014 - 2015 &nbsp;Brenwick Capital , All Rights Reserved.</div>
<div class="abs social"><span></span><span></span><span></span><span></span><span></span></div>

</body>
</html>
```